Zielgruppe
Massagen und Therapien an Patienten mit Schmerzen an Muskeln und am gesamten Bewegungsapparat. Nachbehandlung nach Operationen und Verletzungen sowie Sportverletzungen therapieren.
Zielgruppe: alle Personen (m/w) jeden alters egal ob sportlich oder 'faul'.
Aufgabenstellung
Das Design soll Ruhe, Harmonie, Vertrautheit und Geborgenheit vermitteln. Es muß mit dem Firmenlogo harmonisieren (Farbe und Gestaltung).
Das Logo und der Text findet sich im Anhang.
Es können Bilder eigenständig hinzugefügt werden.
Unbedingt DIN-Format verwenden (welches bleibt dem Designer überlassen)

```html
<!DOCTYPE html>
<html lang="de">
<head>
<meta charset="utf-8">
<title>Massagepraxis – Leistungen</title>
<link href="https://fonts.googleapis.com/css2?family=Merriweather:wght@300;400&family=Gochi+Hand&display=swap" rel="stylesheet">
<style>
  :root {
    --green: #a2c530;
    --green-light: #c9dd86;
    --blue: #4f93cf;
    --ink: #1b1b1b;
    --paper: #ffffff;
  }
  * { margin: 0; padding: 0; box-sizing: border-box; }
  html, body { width: 1200px; height: 848px; overflow: hidden; background: var(--paper); }
  .sheet {
    position: relative; width: 1200px; height: 848px; overflow: hidden;
    font-family: "Merriweather", Georgia, serif; font-weight: 300;
    color: var(--ink); font-size: 13.6px; line-height: 21.4px;
  }
  .header-band {
    position: absolute; left: 0; top: 0; width: 1200px; height: 68px;
    background: var(--green);
  }
  .column { position: absolute; top: 0; width: 340px; }
  .column--massage { left: 33px; }
  .column--lymph { left: 436px; }
  .column--akupunkt { left: 840px; width: 340px; }
  .column-title {
    height: 68px; display: flex; align-items: center;
    color: #fff; font-weight: 400; font-size: 20.5px; letter-spacing: .2px;
    white-space: nowrap;
  }
  .intro { margin-top: 30px; }
  .column--lymph .intro { margin-top: 32px; }
  .section-label { color: var(--blue); margin-top: 21px; }
  .list { list-style: none; }
  .list li { position: relative; padding-left: 12px; }
  .list li::before { content: "•"; position: absolute; left: 1px; }
  .list--indications li { color: var(--blue); }
  .list--effects { margin-top: 21px; }
  .note { margin-top: 21px; }
  .quote {
    position: absolute; left: 880px; top: 368px; width: 250px;
    text-align: center; color: var(--green);
    font-family: "Gochi Hand", cursive; font-size: 30px; line-height: 34px;
  }
  .quote-author {
    position: absolute; left: 1012px; top: 474px;
    font-size: 11.5px; font-weight: 400; color: var(--ink);
  }
  .photo-area { position: absolute; left: 0; top: 546px; width: 1200px; height: 302px; }
</style>
</head>
<body>
<div class="sheet">
  <div class="header-band"></div>

  <section class="column column--massage">
    <h2 class="column-title">Massage</h2>
    <p class="intro">Die klassische Massage dient vor allem zur Behandlungverspannter Muskulatur, oder zur Vorbeugung vonVerspannungen.</p>
    <p class="section-label">Indikationen:</p>
    <ul class="list list--indications">
      <li>Bewegungseinschränkung durch Verspann-<br>ungen am Rücken, Brust, Schulter,etc...</li>
      <li>Spannungskopfschmerzen</li>
      <li>Muskelschmerzen</li>
      <li>zur schnellen Regeneration nach dem<br>Sport oder nach Verletzungen</li>
      <li>fördert die seelische und körperliche<br>Ausgeglichenheit</li>
      <li>stabilisiert das Immunsystem</li>
      <li>verbessert den Lymphfluss</li>
      <li>wirkt sich positiv auf die Durchblutung der<br>Haut und des Bindegewebes aus</li>
    </ul>
    <p class="note">Die Massagetherapie wird nach ärztlicher<br>Verordnung durchgeführt.</p>
  </section>

  <section class="column column--lymph">
    <h2 class="column-title">Lymphdrainage</h2>
    <p class="intro">Die sanften, schmerzfreien und langsam ausge-<br>führten Griffe wirken</p>
    <ul class="list list--effects">
      <li>Entwässernd —&gt; entstauend</li>
      <li>Entgiftend —&gt; entschlakend</li>
      <li>Beruhigend —&gt; entspannend</li>
      <li>stärken das Immunsystem</li>
      <li>bei Rheumatische Schwellungen</li>
    </ul>
    <p class="section-label">Indikationen:</p>
    <ul class="list list--indications">
      <li>nach Operationen</li>
      <li>nach Tumorbehandlungen</li>
      <li>nach Verletzungen</li>
      <li>nach Lymphknotenentfernungen</li>
      <li>nach Hämatomen (Bluterguß)</li>
      <li>hoher Muskeltonus</li>
    </ul>
    <p class="note">Über das Lymphsystem werden die meisten Ab-<br>fallprodukte des Körpers abtransportiert.</p>
  </section>

  <section class="column column--akupunkt">
    <h2 class="column-title">Akupunk-Massage nach Hollmer</h2>
    <p class="intro">Durch diese Behandlungsmethode können viele Beschwerde- und Krankheitsbilder beeinflusst werden die durch funktionelle Stö-<br>rungen im Körper verursacht worden sind.</p>
    <p class="section-label">Indikationen:</p>
    <ul class="list list--indications">
      <li>Wirbelsäulenbeschwerden</li>
      <li>Migräne</li>
      <li>Erkrankungen der Gelenke</li>
      <li>Neuralgien</li>
      <li>Durchblutungsstörungen</li>
    </ul>
  </section>

  <p class="quote">„Hier könnte ein Zitat zum Thema Massage stehen“</p>
  <p class="quote-author">Erika Beispiel</p>

  <svg class="photo-area" width="1200" height="302" viewBox="0 0 1200 302">
    <defs>
      <linearGradient id="photoTone" x1="0" y1="0" x2="1" y2="0">
        <stop offset="0" stop-color="#e9e7e4"/>
        <stop offset="0.45" stop-color="#e4cbb6"/>
        <stop offset="0.8" stop-color="#efe7e0"/>
        <stop offset="1" stop-color="#f2f2f2"/>
      </linearGradient>
    </defs>
    <rect width="1200" height="302" fill="url(#photoTone)" role="img" aria-label="Foto: Frau liegt entspannt auf einer Liege und erhält eine Rückenmassage"/>
    <rect width="1200" height="42" fill="#ffffff" opacity="0.45"/>
    <path d="M0 118 C 250 200, 650 270, 1200 282 L1200 302 L0 302 Z" fill="var(--green-light)" opacity="0.8"/>
    <path d="M0 150 C 260 230, 680 282, 1200 290 L1200 302 L0 302 Z" fill="var(--green)"/>
  </svg>
</div>
</body>
</html>
```